Talvon Crest Real estate in need of Logo design

I just started a new real estate brokerage company and need a professional, new logo design that I can incorporate through all forms of marketing and branding. I would like the business card to use both Matte finish and high gloss.

```html
<!DOCTYPE html>
<html lang="en">
<head>
<meta charset="utf-8">
<title>Talvon Crest Real Estate — Business Card</title>
<link rel="stylesheet" href="https://fonts.googleapis.com/css2?family=Cinzel:wght@400;600&family=Lato:wght@400&display=swap">
<style>
  :root {
    --page-bg: #1a1a1c;
    --card-bg: #121214;
    --brand-blue: #1f3f9e;
    --silver: #d9d9dc;
    --text-light: #e4e4e6;
    --text-muted: #b5b5b8;
    --rule: #5b5b60;
  }
  * { box-sizing: border-box; margin: 0; padding: 0; }
  html, body { width: 1200px; height: 900px; overflow: hidden; }
  body {
    background: var(--page-bg);
    font-family: "Lato", sans-serif;
    position: relative;
  }
  .card {
    position: absolute;
    width: 560px;
    height: 320px;
    background: var(--card-bg);
    border-radius: 22px;
    box-shadow: 0 18px 40px rgba(0,0,0,.55);
  }
  .card--front { left: 320px; top: 70px; display: flex; align-items: center; justify-content: center; }
  .card--back { left: 320px; top: 470px; }

  .front-mark {
    font-family: "Cinzel", serif;
    font-weight: 600;
    font-size: 38px;
    letter-spacing: 4px;
    color: var(--silver);
  }

  .lockup {
    position: absolute;
    top: 44px;
    right: 40px;
    display: flex;
    align-items: center;
    gap: 16px;
  }
  .lockup__square { width: 34px; height: 34px; background: var(--brand-blue); }
  .lockup__text { text-align: center; }
  .lockup__name {
    font-family: "Cinzel", serif;
    font-size: 27px;
    color: var(--brand-blue);
    letter-spacing: 1px;
    line-height: 1;
  }
  .lockup__tagline {
    display: flex;
    align-items: center;
    gap: 8px;
    margin-top: 6px;
    font-family: "Cinzel", serif;
    font-size: 13px;
    letter-spacing: 3px;
    color: var(--text-muted);
  }
  .lockup__tagline::before, .lockup__tagline::after {
    content: ""; flex: 1; height: 1px; background: var(--rule);
  }
  .header-rule {
    position: absolute; left: 40px; right: 40px; top: 118px;
    height: 1px; background: var(--rule);
  }

  .person { position: absolute; left: 40px; top: 168px; }
  .person__name {
    font-family: "Cinzel", serif;
    font-size: 22px;
    color: var(--brand-blue);
    letter-spacing: 1px;
  }
  .person__role { font-size: 16px; color: var(--text-light); margin-top: 2px; }
  .name-rule {
    position: absolute; left: 220px; right: 40px; top: 186px;
    height: 1px; background: var(--rule);
  }

  .address {
    position: absolute; right: 40px; top: 140px;
    text-align: right; font-size: 15px; line-height: 1.4; color: var(--text-light);
  }

  .contacts { position: absolute; left: 40px; top: 232px; list-style: none; }
  .contacts__item {
    display: flex; align-items: center; gap: 10px;
    font-size: 16px; color: var(--text-light); line-height: 1.45;
  }
  .contacts__icon { width: 13px; height: 13px; fill: var(--brand-blue); flex: none; }
</style>
</head>
<body>
  <section class="card card--front" aria-label="Card front">
    <span class="front-mark">TALVON CREST</span>
  </section>

  <section class="card card--back" aria-label="Card back">
    <div class="lockup">
      <span class="lockup__square"></span>
      <div class="lockup__text">
        <div class="lockup__name">TALVON CREST</div>
        <div class="lockup__tagline">REAL ESTATE</div>
      </div>
    </div>
    <div class="header-rule"></div>

    <div class="person">
      <div class="person__name">MARCUS HALE</div>
      <div class="person__role">Managing Director</div>
    </div>
    <div class="name-rule"></div>

    <address class="address" style="font-style:normal">
      87, Harbor View Lane<br>Westbrook, 20931
    </address>

    <ul class="contacts">
      <li class="contacts__item">
        <svg class="contacts__icon" viewBox="0 0 16 16"><path d="M3 1h3l1.5 4-2 1.3a9 9 0 0 0 4.2 4.2L11 8.5l4 1.5v3a2 2 0 0 1-2 2A12 12 0 0 1 1 3a2 2 0 0 1 2-2z"/></svg>
        044-210 387 554
      </li>
      <li class="contacts__item">
        <svg class="contacts__icon" viewBox="0 0 16 16"><path d="M1 3h14v10H1z M1 3l7 6 7-6" stroke="#121214" stroke-width="1.2"/></svg>
        info@talvoncrest.com
      </li>
      <li class="contacts__item">
        <svg class="contacts__icon" viewBox="0 0 16 16"><circle cx="8" cy="8" r="7"/><path d="M1 8h14M8 1c-3 3.5-3 10.5 0 14M8 1c3 3.5 3 10.5 0 14" stroke="#121214" stroke-width="1" fill="none"/></svg>
        www.talvoncrest.com
      </li>
    </ul>
  </section>
</body>
</html>
```